Ladles and Lanterns App design

I need a full app design, colours, images, fonts, and a mock up design of the app to bring to the developer.

Ladles and Lanterns is a free app that allows cafes, independent cafe and chains of cafes to let their customers know what the soup of the day and what specials they have on that day through the app. Each cafe will have a profile which they can upload the Ladles and Lanterns daily.

The user home screen will include google maps showing their location with the registered cafes and eateries around them. including a list of the cafe and distances below. as seen in attachment.

Target Market(s)

Cafes , anyone who enjoys eating soups and off local cafe specials boards

Requirements
Must have
• I would like a complete app design based on the attached images.

```html
<!DOCTYPE html>
<html lang="en">
<head>
<meta charset="utf-8">
<title>Ladles and Lanterns – App Screens</title>
<link href="https://fonts.googleapis.com/css2?family=Poppins:wght@400;500;600;700&display=swap" rel="stylesheet">
<style>
  :root{
    --bg:#FDB940;
    --accent:#FBB12E;
    --price:#F5A623;
    --heart:#F0304F;
    --white:#FFFFFF;
    --screen:#F7F7F7;
    --ink:#2B2B2B;
    --muted:#9A9A9A;
    --line:#E6E6E6;
    --photo-a:#5E6670;
    --photo-b:#9AA3AB;
    --soup:#E8692A;
    --green:#3CCB6B;
  }
  *{box-sizing:border-box;margin:0;padding:0}
  html,body{width:1200px;height:675px;overflow:hidden}
  body{background:var(--bg);font-family:'Poppins',sans-serif;color:var(--ink);position:relative}
  .page-title{position:absolute;left:88px;top:38px;font-size:21px;font-weight:700;color:var(--white)}
  .footnote{position:absolute;right:88px;top:614px;font-size:13px;color:var(--white)}

  .screen{position:absolute;top:110px;width:236px;height:480px;background:var(--screen);border-radius:26px;overflow:hidden;box-shadow:0 18px 40px rgba(120,70,0,.25)}
  .screen--home{left:200px}
  .screen--item{left:482px}
  .screen--cafe{left:764px}

  /* home */
  .home-header{position:absolute;left:0;top:0;width:100%;height:120px;background:var(--white)}
  .brand-square{position:absolute;left:16px;top:30px;width:34px;height:34px;border-radius:8px;background:var(--accent)}
  .settings{position:absolute;right:16px;top:32px;width:16px;height:16px}
  .search{position:absolute;left:16px;top:78px;right:16px;height:28px;border:1px solid var(--line);border-radius:8px;font-size:10px;color:var(--muted);padding:6px 10px;display:flex;align-items:center;gap:6px}
  .search-dot{width:7px;height:7px;border-radius:50%;background:var(--muted)}
  .map{position:absolute;left:0;top:120px;width:100%;height:360px;background:linear-gradient(160deg,#F0F0F0,#E3E3E3)}
  .pin-label{position:absolute;background:var(--white);border-radius:6px;padding:4px 8px;font-size:8.5px;font-weight:500;display:flex;align-items:center;gap:5px;box-shadow:0 2px 6px rgba(0,0,0,.08);white-space:nowrap}
  .pin-label .bowl{width:10px;height:6px;border-radius:0 0 6px 6px;background:var(--soup)}
  .my-location{position:absolute;left:178px;top:338px;width:26px;height:26px}
  .tabbar{position:absolute;left:14px;right:14px;bottom:16px;height:40px;background:var(--white);border-radius:20px;display:flex;justify-content:space-around;align-items:center;box-shadow:0 4px 12px rgba(0,0,0,.08)}
  .tabbar svg{width:16px;height:16px}

  /* hero */
  .hero{position:absolute;left:0;top:0;width:100%;height:170px;background:radial-gradient(circle at 58% 52%,var(--soup) 0 32px,#DADADA 33px 41px,transparent 42px),linear-gradient(135deg,var(--photo-b),var(--photo-a))}
  .hero-shade{position:absolute;inset:0;background:linear-gradient(180deg,rgba(0,0,0,.05) 40%,rgba(0,0,0,.5))}
  .hero-nav{position:absolute;left:14px;top:22px;right:14px;display:flex;align-items:center;gap:10px;color:var(--white);font-size:9px}
  .hero-nav .back{font-size:13px}
  .hero-nav .caption{flex:1;text-align:center;margin-right:20px}
  .hero-title{position:absolute;left:16px;top:138px;color:var(--white);font-weight:600;font-size:16px;line-height:1.2}
  .hero-title--with-sub{top:122px}
  .hero-sub{display:block;font-size:9px;font-weight:400}
  .fav-btn{position:absolute;right:16px;top:128px;width:26px;height:26px;border-radius:50%;background:var(--white);display:flex;align-items:center;justify-content:center}
  .fav-btn--accent{background:var(--accent);border-radius:6px;width:22px;height:22px;top:96px}

  .section-label{position:absolute;left:16px;font-size:10px;color:#555}
  .venue-card{position:absolute;left:12px;right:12px;height:110px;background:var(--white);border-radius:10px;padding:14px 14px}
  .venue-head{display:flex;gap:8px;align-items:flex-start}
  .venue-pin{width:18px;height:18px;border-radius:50%;background:var(--accent);flex:none;display:flex;align-items:center;justify-content:center}
  .venue-pin i{width:5px;height:5px;border-radius:50%;background:var(--ink)}
  .venue-name{font-size:10px;font-weight:600}
  .venue-addr{font-size:7.5px;color:var(--muted)}
  .venue-price{position:absolute;right:14px;top:10px;font-size:9px;font-weight:600;color:var(--price)}
  .btn{position:absolute;right:14px;bottom:14px;width:118px;height:28px;border-radius:8px;background:var(--accent);color:var(--ink);font-size:9.5px;font-weight:500;display:flex;align-items:center;justify-content:center}

  .menu-row{position:absolute;left:12px;right:12px;height:44px;background:var(--white);border-radius:10px;display:flex;align-items:center;gap:10px;padding:0 12px}
  .thumb{width:26px;height:26px;border-radius:50%;background:radial-gradient(circle,var(--soup) 0 7px,#D8D8D8 8px 11px,#B8BEC4 12px);position:relative;flex:none}
  .thumb--drink{border-radius:6px;background:linear-gradient(180deg,#F7D9D9,#E06060)}
  .thumb .dot{position:absolute;right:-2px;top:-2px;width:6px;height:6px;border-radius:50%;background:var(--green)}
  .menu-name{flex:1;font-size:10px;font-weight:600}
  .heart{width:12px;height:12px}
  .cafe-footer{position:absolute;left:0;right:0;bottom:0;height:62px;background:var(--white);border-top:1px solid var(--line)}
  .toggle{position:absolute;left:18px;top:26px;width:28px;height:6px;border-radius:3px;background:var(--line)}
  .toggle::after{content:"";position:absolute;right:-2px;top:-2px;width:7px;height:7px;border-radius:50%;background:var(--green)}
</style>
</head>
<body>
  <h1 class="page-title">Ladles and Lanterns</h1>

  <section class="screen screen--home">
    <header class="home-header">
      <div class="brand-square"></div>
      <svg class="settings" viewBox="0 0 16 16"><circle cx="8" cy="8" r="5.5" fill="none" stroke="var(--accent)" stroke-width="3" stroke-dasharray="2.4 1.4"/><circle cx="8" cy="8" r="2" fill="var(--accent)"/></svg>
      <div class="search"><span class="search-dot"></span>Search</div>
    </header>
    <div class="map" role="img" aria-label="Street map of the surrounding area with nearby cafes"></div>
    <div class="pin-label" style="left:20px;top:140px"><span class="bowl"></span>Tova's Table</div>
    <div class="pin-label" style="left:140px;top:128px"><span class="bowl"></span>Tova's Table</div>
    <div class="pin-label" style="left:118px;top:178px"><span class="bowl"></span>Tova's Table</div>
    <div class="pin-label" style="left:44px;top:222px"><span class="bowl"></span>Cafe Maren</div>
    <div class="pin-label" style="left:140px;top:250px"><span class="bowl"></span>Brothwell</div>
    <div class="pin-label" style="left:26px;top:282px"><span class="bowl"></span>Pell Soups</div>
    <div class="pin-label" style="left:84px;top:326px"><span class="bowl"></span>Corner Cafe</div>
    <div class="pin-label" style="left:20px;top:372px"><span class="bowl"></span>Tova's Table</div>
    <svg class="my-location" viewBox="0 0 26 26"><circle cx="13" cy="13" r="12" fill="var(--accent)"/><path d="M13 7a4 4 0 0 1 4 4c0 3-4 7-4 7s-4-4-4-7a4 4 0 0 1 4-4z" fill="var(--ink)"/></svg>
    <nav class="tabbar">
      <svg viewBox="0 0 16 16"><path d="M2 8l6-5 6 5v6H2z" fill="var(--accent)"/></svg>
      <svg viewBox="0 0 16 16"><rect x="3" y="2" width="10" height="12" rx="1.5" fill="#777"/><path d="M5 6h6M5 9h6M5 12h4" stroke="#fff" stroke-width="1.2"/></svg>
      <svg viewBox="0 0 16 16"><path d="M8 14S2 10 2 6a3 3 0 0 1 6-1 3 3 0 0 1 6 1c0 4-6 8-6 8z" fill="#777"/></svg>
      <svg viewBox="0 0 16 16"><circle cx="8" cy="5" r="3" fill="#777"/><path d="M2 15a6 6 0 0 1 12 0z" fill="#777"/></svg>
    </nav>
  </section>

  <section class="screen screen--item">
    <div class="hero" role="img" aria-label="Photo of a bowl of red tomato soup with seeds and herbs"><div class="hero-shade"></div></div>
    <div class="hero-nav"><span class="back">‹</span><span class="caption">Item Details</span></div>
    <div class="fav-btn"><svg class="heart" viewBox="0 0 16 16"><path d="M8 14S2 10 2 6a3 3 0 0 1 6-1 3 3 0 0 1 6 1c0 4-6 8-6 8z" fill="none" stroke="var(--heart)" stroke-width="1.6"/></svg></div>
    <h2 class="hero-title">Red Hot Soup</h2>
    <p class="section-label" style="top:184px">Available here:</p>
    <article class="venue-card" style="top:208px">
      <div class="venue-head"><span class="venue-pin"><i></i></span><div><p class="venue-name">Cafe Maren</p><p class="venue-addr">Unit 12, Harbor Lane, Oakridge</p></div></div>
      <span class="venue-price">$5.99</span>
      <span class="btn">Get Directions</span>
    </article>
    <article class="venue-card" style="top:330px">
      <div class="venue-head"><span class="venue-pin"><i></i></span><div><p class="venue-name">Tova's Table</p><p class="venue-addr">B-7, Linden Court, Westvale</p></div></div>
      <span class="venue-price">$4.65</span>
      <span class="btn">Get Directions</span>
    </article>
  </section>

  <section class="screen screen--cafe">
    <div class="hero" role="img" aria-label="Photo of a bowl of orange soup on a grey table"><div class="hero-shade"></div></div>
    <div class="hero-nav"><span class="back">‹</span><span class="caption">Cafe Details</span></div>
    <div class="fav-btn fav-btn--accent"></div>
    <h2 class="hero-title hero-title--with-sub">Cafe Maren<span class="hero-sub">The best in town for soups!</span></h2>
    <p class="section-label" style="top:182px">Soups</p>
    <div class="menu-row" style="top:202px"><span class="thumb" role="img" aria-label="Red Hot Soup dish photo"><span class="dot"></span></span><span class="menu-name">Red Hot Soup</span><svg class="heart" viewBox="0 0 16 16"><path d="M8 14S2 10 2 6a3 3 0 0 1 6-1 3 3 0 0 1 6 1c0 4-6 8-6 8z" fill="var(--heart)"/></svg></div>
    <div class="menu-row" style="top:252px"><span class="thumb" role="img" aria-label="Veggie Soup dish photo"><span class="dot"></span></span><span class="menu-name">Veggie Soup</span><svg class="heart" viewBox="0 0 16 16"><path d="M8 14S2 10 2 6a3 3 0 0 1 6-1 3 3 0 0 1 6 1c0 4-6 8-6 8z" fill="var(--heart)"/></svg></div>
    <p class="section-label" style="top:310px">Specials</p>
    <div class="menu-row" style="top:330px"><span class="thumb thumb--drink" role="img" aria-label="Strawberry smoothie photo"></span><span class="menu-name">Strawberry Smoothie</span><svg class="heart" viewBox="0 0 16 16"><path d="M8 14S2 10 2 6a3 3 0 0 1 6-1 3 3 0 0 1 6 1c0 4-6 8-6 8z" fill="var(--heart)"/></svg></div>
    <footer class="cafe-footer"><span class="toggle"></span><span class="btn" style="bottom:17px">Get Directions</span></footer>
  </section>

  <p class="footnote">Please check the prototype for full experience!</p>
</body>
</html>
```